Bref créative
BRN Tek
B-cards, letter head and envelopes
I need single sided standard sized Business Card [3.5" x 2"]
use same font or others...other fonts are welcome
Simple
Gareth Pembly
CEO
482 Harlowe Street, Suite 1730
Larkmont, Oregon 97402
gpembly@brnqel.com
brnqel.com
-use this logo in the business cards, letterhead and envelopes.
-we are looking for designs with and with out a water mark using parts or the entire logo.

```html
<!DOCTYPE html>
<html lang="en">
<head>
<meta charset="utf-8">
<title>BRN Tek Stationery</title>
<link href="https://fonts.googleapis.com/css2?family=Open+Sans:wght@400;600;700;800&display=swap" rel="stylesheet">
<style>
  :root {
    --green: #8cc63f;
    --green-faint: #e6f2d6;
    --blue: #2c4a7b;
    --ink: #5a5a5a;
    --paper: #ffffff;
    --backdrop: #ffffff;
    --edge: #d9d9d9;
  }
  * { margin: 0; padding: 0; box-sizing: border-box; }
  html, body { width: 1200px; height: 703px; overflow: hidden; background: var(--backdrop); }
  body { position: relative; font-family: "Open Sans", Arial, sans-serif; color: var(--ink); }

  .sheet {
    position: absolute; background: var(--paper); overflow: hidden;
    border: 1px solid var(--edge);
    box-shadow: 0 6px 10px -6px rgba(0,0,0,0.35);
  }
  .brand {
    position: absolute; display: flex; align-items: center; gap: 5px;
    font-weight: 800; color: var(--green); letter-spacing: 1px; line-height: 1;
    white-space: nowrap;
  }
  .brand-dot { border-radius: 50%; background: var(--green); flex: none; }
  .address { position: absolute; font-size: 7px; line-height: 1.45; color: var(--ink); white-space: nowrap; }
  .watermark {
    position: absolute; font-weight: 800; color: var(--green-faint); letter-spacing: 2px; line-height: 1;
  }

  /* envelope back */
  .envelope-back { left: 29px; top: 19px; width: 470px; height: 144px; }
  .envelope-back .flap { position: absolute; left: 0; top: 0; }
  .envelope-back .brand { left: 206px; top: 34px; font-size: 30px; color: var(--paper); }
  .envelope-back .brand-dot { width: 10px; height: 10px; background: var(--paper); }

  /* envelope front */
  .envelope-front { left: 29px; top: 185px; width: 470px; height: 211px; }
  .envelope-front .brand { left: 22px; top: 26px; font-size: 34px; }
  .envelope-front .brand-dot { width: 11px; height: 11px; }
  .envelope-front .address { left: 140px; top: 30px; padding-left: 8px; border-left: 1px solid var(--edge); }
  .envelope-front .watermark { right: 20px; bottom: 16px; font-size: 40px; }

  /* DL envelope */
  .envelope-dl { left: 29px; top: 432px; width: 470px; height: 221px; }
  .envelope-dl .brand { left: 22px; top: 30px; font-size: 34px; }
  .envelope-dl .brand-dot { width: 11px; height: 11px; }
  .envelope-dl .address { left: 22px; bottom: 18px; font-size: 6px; }
  .envelope-dl .corner { position: absolute; right: 0; bottom: 0; }

  /* letterhead */
  .letterhead { left: 523px; top: 19px; width: 377px; height: 641px; }
  .letterhead .brand { left: 24px; top: 28px; font-size: 34px; }
  .letterhead .brand-dot { width: 11px; height: 11px; }
  .letterhead .address { left: 155px; top: 33px; }
  .letterhead .watermark { right: 30px; bottom: 30px; font-size: 48px; }
  .letterhead .foot-band { position: absolute; left: 0; right: 0; bottom: 0; height: 5px; background: var(--green); }

  /* business cards */
  .card { left: 924px; width: 252px; height: 106px; }
  .card .brand { font-size: 22px; }
  .card .brand-dot { width: 7px; height: 7px; }
  .card .person { position: absolute; font-size: 9px; font-weight: 700; color: var(--blue); line-height: 1.3; }
  .card .role { display: block; font-size: 6px; font-weight: 400; color: var(--ink); }
  .card .address { font-size: 5.5px; line-height: 1.5; }

  .card-one { top: 19px; }
  .card-one .person { right: 18px; top: 10px; text-align: right; }
  .card-one .brand { left: 16px; top: 44px; }
  .card-one .address { left: 122px; top: 40px; }

  .card-two { top: 149px; height: 101px; }
  .card-two .brand { left: 16px; top: 14px; }
  .card-two .address { left: 120px; top: 12px; }
  .card-two .person { left: 16px; top: 62px; }

  .card-three { top: 264px; height: 103px; }
  .card-three .person { left: 0; right: 0; top: 8px; text-align: center; }
  .card-three .brand { left: 16px; top: 50px; }
  .card-three .address { left: 120px; top: 44px; }

  .card-four { top: 384px; height: 108px; background: var(--blue); border-color: var(--blue); }
  .card-four .person { left: 16px; top: 22px; color: var(--paper); }
  .card-four .person .role { color: var(--paper); }
  .card-four .brand { left: 16px; top: 62px; color: var(--paper); }
  .card-four .brand-dot { background: var(--paper); }
  .card-four .address { left: 128px; top: 20px; color: var(--paper); }

  .card-five { top: 509px; height: 108px; background: var(--green); border-color: var(--green); }
  .card-five .panel { position: absolute; left: 12px; top: 14px; width: 100px; height: 80px; background: var(--paper); }
  .card-five .brand { left: 22px; top: 26px; }
  .card-five .person { left: 22px; top: 60px; }
  .card-five .address { left: 126px; top: 20px; color: var(--paper); }
</style>
</head>
<body>

<section class="sheet envelope-back" aria-label="Envelope back">
  <svg class="flap" width="470" height="144" viewBox="0 0 470 144" aria-hidden="true">
    <path d="M0 0 H470 V14 L235 78 L0 14 Z" fill="var(--green)"/>
  </svg>
  <div class="brand"><span class="brand-dot"></span>BRN</div>
</section>

<section class="sheet envelope-front" aria-label="Envelope front">
  <div class="brand"><span class="brand-dot"></span>BRN</div>
  <p class="address">482 Harlowe Street, Suite 1730<br>Larkmont, Oregon 97402</p>
  <div class="watermark">BRN</div>
</section>

<section class="sheet envelope-dl" aria-label="DL envelope">
  <div class="brand"><span class="brand-dot"></span>BRN</div>
  <p class="address">482 Harlowe Street, Suite 1730 Larkmont, Oregon 97402</p>
  <svg class="corner" width="70" height="70" viewBox="0 0 70 70" aria-hidden="true">
    <circle cx="70" cy="70" r="56" fill="var(--blue)"/>
  </svg>
</section>

<section class="sheet letterhead" aria-label="Letterhead">
  <div class="brand"><span class="brand-dot"></span>BRN</div>
  <p class="address">482 Harlowe Street, Suite 1730<br>Larkmont, Oregon 97402</p>
  <div class="watermark">BRN</div>
  <div class="foot-band"></div>
</section>

<section class="sheet card card-one" aria-label="Business card">
  <p class="person">Gareth Pembly<span class="role">CEO</span></p>
  <div class="brand"><span class="brand-dot"></span>BRN</div>
  <p class="address">482 Harlowe Street, Suite 1730<br>Larkmont, Oregon 97402<br>T: 541 555 0182<br>gpembly@brnqel.com<br>brnqel.com</p>
</section>

<section class="sheet card card-two" aria-label="Business card">
  <div class="brand"><span class="brand-dot"></span>BRN</div>
  <p class="address">482 Harlowe Street, Suite 1730<br>Larkmont, Oregon 97402<br>T: 541 555 0182<br>gpembly@brnqel.com<br>brnqel.com</p>
  <p class="person">Gareth Pembly<span class="role">CEO</span></p>
</section>

<section class="sheet card card-three" aria-label="Business card">
  <p class="person">Gareth Pembly<span class="role">CEO</span></p>
  <div class="brand"><span class="brand-dot"></span>BRN</div>
  <p class="address">482 Harlowe Street, Suite 1730<br>Larkmont, Oregon 97402<br>T: 541 555 0182<br>gpembly@brnqel.com<br>brnqel.com</p>
</section>

<section class="sheet card card-four" aria-label="Business card">
  <p class="person">Gareth Pembly<span class="role">CEO</span></p>
  <div class="brand"><span class="brand-dot"></span>BRN</div>
  <p class="address">482 Harlowe Street, Suite 1730<br>Larkmont, Oregon 97402<br>T: 541 555 0182<br>gpembly@brnqel.com<br>brnqel.com</p>
</section>

<section class="sheet card card-five" aria-label="Business card">
  <div class="panel"></div>
  <div class="brand"><span class="brand-dot"></span>BRN</div>
  <p class="person">Gareth Pembly<span class="role">CEO</span></p>
  <p class="address">482 Harlowe Street, Suite 1730<br>Larkmont, Oregon 97402<br>T: 541 555 0182<br>gpembly@brnqel.com<br>brnqel.com</p>
</section>

</body>
</html>
```